Martin Hale PA Card Logo

Current logo attached. Its 25 year old logo I have used. Looking for a new fresh elegant professional look/design for a law firm that has high net worth clientele and is estate planning business law firm. Firm mis in Palm Beach Florida.
One sided card linen stock white will be used. Logo section name section. Logo should include nice elegant design using the letter "M" perhapa (I am not wed to current font of the M on current logo.) Be creative there with logo design. My initials are MH.......color scheme I figure 3 tone... Raised Gold Foil, Blue name of firm = Martin Hale, P.A. My practice focus is Family and Business Asset Protection. My name is Martin M. Hale, Esq. Practice specialties include Asset Protection trusts, Business Succession Planning, LLC law, Estate Planning, Medicaid Planning (Maybe put those topics in bullets in a section of card. Bottom of card can be reserved smaller print address phone website and email address. Address section is not as important as logo and topics of practice on front. I foresee address section can be in dark blue. MY name and Topics dark blue as well.
Target Market(s)
affluent; business owners executives; wealth 2-10 million net worth
Industry/Entity Type
business law and estate planning
Contact Information for Business Card
White thick linen one sided

```html
<!DOCTYPE html>
<html lang="en">
<head>
<meta charset="utf-8">
<title>Martin Hale, P.A. – Business Card</title>
<link href="https://fonts.googleapis.com/css2?family=Cinzel:wght@600&family=PT+Sans:wght@700&display=swap" rel="stylesheet">
<style>
  :root {
    --backdrop: #ebebeb;
    --navy: #003c6e;
    --gold: #b9a236;
    --paper: #ffffff;
    --ink: #111111;
    --rule: #50627a;
  }
  html, body {
    margin: 0;
    width: 1200px;
    height: 1200px;
    overflow: hidden;
    background: var(--backdrop);
  }
  .canvas { position: relative; width: 1200px; height: 1200px; }
  .card {
    position: absolute;
    left: 232px;
    width: 733px;
    height: 418px;
    border-radius: 40px;
    overflow: hidden;
  }
  .card--front { top: 135px; background: var(--navy); }
  .card--back { top: 650px; height: 416px; background: var(--paper); }

  .front-name {
    position: absolute;
    left: 0; right: 0;
    top: 183px;
    text-align: center;
    font-family: "Cinzel", serif;
    font-weight: 600;
    font-size: 42px;
    color: var(--gold);
    margin: 0;
  }

  .brand-dot {
    position: absolute;
    left: 108px; top: 100px;
    width: 52px; height: 52px;
    border-radius: 50%;
    background: var(--gold);
  }
  .firm-name {
    position: absolute;
    left: 210px; top: 84px;
    margin: 0;
    font-family: "Cinzel", serif;
    font-weight: 600;
    font-size: 42px;
    line-height: 1.2;
    color: var(--gold);
    white-space: nowrap;
  }
  .firm-tagline {
    position: absolute;
    left: 211px; top: 134px;
    margin: 0;
    font-family: "Cinzel", serif;
    font-weight: 600;
    font-size: 22px;
    color: var(--gold);
    white-space: nowrap;
  }
  .divider {
    position: absolute;
    left: 52px; top: 204px;
    width: 637px; height: 0;
    border-top: 1.5px solid var(--rule);
  }
  .contacts {
    position: absolute;
    left: 50px; top: 215px;
    margin: 0; padding: 0;
    list-style: none;
    font-family: "PT Sans", sans-serif;
    font-weight: 700;
    font-size: 16px;
    color: var(--ink);
  }
  .contacts li {
    display: flex;
    align-items: center;
    height: 27px;
  }
  .contacts svg { width: 22px; height: 22px; margin-right: 10px; }
  .address {
    position: absolute;
    right: 38px; top: 276px;
    margin: 0;
    text-align: right;
    font-family: "PT Sans", sans-serif;
    font-weight: 700;
    font-size: 16px;
    line-height: 22px;
    color: var(--ink);
  }
  .swoosh { position: absolute; left: 0; top: 0; width: 733px; height: 416px; }
</style>
</head>
<body>
<main class="canvas">

  <section class="card card--front" aria-label="Card front">
    <p class="front-name">Martin Hale, P.A.</p>
  </section>

  <section class="card card--back" aria-label="Card back">
    <svg class="swoosh" viewBox="0 0 733 416" aria-hidden="true">
      <path d="M0 368 Q 420 372 733 330 L733 416 L0 416 Z" fill="var(--navy)"/>
      <path d="M0 338 Q 260 362 518 355 Q 260 368 0 352 Z" fill="var(--gold)"/>
    </svg>

    <span class="brand-dot" aria-hidden="true"></span>
    <h1 class="firm-name">Martin Hale, P.A.</h1>
    <p class="firm-tagline">Elder Law Attorney</p>

    <div class="divider"></div>

    <ul class="contacts">
      <li>
        <svg viewBox="0 0 22 22" aria-hidden="true"><circle cx="11" cy="11" r="9.5" fill="none" stroke="var(--rule)" stroke-width="1.3"/><path d="M7.5 6.5 L9.5 6 L10.5 8.5 L9.3 9.5 Q10.5 12 12.8 13 L13.8 11.8 L16 12.8 L15.5 15 Q10 15.5 7 9.5 Z" fill="var(--rule)"/></svg>
        555 010 8456
      </li>
      <li>
        <svg viewBox="0 0 22 22" aria-hidden="true"><circle cx="11" cy="11" r="9.5" fill="none" stroke="var(--rule)" stroke-width="1.3"/><rect x="8" y="5.5" width="6" height="11" rx="1" fill="none" stroke="var(--rule)" stroke-width="1.3"/></svg>
        555 010 4569
      </li>
      <li>
        <svg viewBox="0 0 22 22" aria-hidden="true"><circle cx="11" cy="11" r="9.5" fill="none" stroke="var(--rule)" stroke-width="1.3"/><rect x="6" y="7.5" width="10" height="7" fill="var(--rule)"/><path d="M6 7.5 L11 11.5 L16 7.5" fill="none" stroke="#fff" stroke-width="1"/></svg>
        info@martinhalelaw.com
      </li>
      <li>
        <svg viewBox="0 0 22 22" aria-hidden="true"><circle cx="11" cy="11" r="9.5" fill="none" stroke="var(--rule)" stroke-width="1.3"/><circle cx="11" cy="11" r="5.5" fill="none" stroke="var(--rule)" stroke-width="1.1"/><path d="M5.5 11 H16.5 M11 5.5 V16.5 M11 5.5 Q8 11 11 16.5 M11 5.5 Q14 11 11 16.5" fill="none" stroke="var(--rule)" stroke-width="0.9"/></svg>
        www.martinhalelaw.com
      </li>
    </ul>

    <p class="address">P.O. Box, Street Name,<br>Countryname , ZIPCODE 0000</p>
  </section>

</main>
</body>
</html>
```